Flyer for Institute Party

This event has changed to the following - March 24th, 2017 from 4-6pm in the Halvern Medical Education Center Atrium (You can get to the Atrium from the Drentby elevators by getting off on the 5th floor or from the Crestmoor Pavilion elevators by getting off on the 5th floor). I have attached the logo of the Institute as well to add to the flyer. Also, the Lumaris Institute just became and Institute in January 2017, so it would be nice to note that as part of the celebration in the flyer someplace. We have a lot to celebrate! I am looking for a fun flyer to for an Institute party. We would like to celebrate becoming an Institute and the labs within the Institute at the party.

```html
<!DOCTYPE html>
<html lang="en">
<head>
<meta charset="utf-8">
<title>International Day of Awesomeness – Halden Lumaris Institute</title>
<link rel="stylesheet" href="https://fonts.googleapis.com/css2?family=Open+Sans:ital,wght@0,400;0,600;0,700;0,800;1,700&display=swap">
<style>
  :root {
    --paper: #f2f2f3;
    --blue-light: #1a8bbb;
    --blue-mid: #1678a6;
    --blue-deep: #0d4866;
    --navy-text: #10405f;
    --red: #c11f2f;
    --white: #ffffff;
  }
  * { margin: 0; padding: 0; box-sizing: border-box; }
  html, body {
    width: 1017px;
    height: 1200px;
    overflow: hidden;
    background: var(--paper);
  }
  .flyer {
    position: relative;
    width: 1017px;
    height: 1200px;
    background: var(--paper);
    font-family: "Open Sans", Arial, sans-serif;
    overflow: hidden;
  }
  .flyer__shapes {
    position: absolute;
    inset: 0;
    width: 1017px;
    height: 1200px;
  }
  .molecule-art {
    position: absolute;
    left: 330px;
    top: 220px;
    width: 680px;
    height: 520px;
    border-radius: 50%;
    background: radial-gradient(ellipse at 55% 45%, rgba(190, 180, 205, 0.35) 0%, rgba(225, 200, 212, 0.22) 45%, rgba(242, 242, 243, 0) 72%);
  }
  .headline-intro {
    position: absolute;
    left: 28px;
    top: 36px;
    color: var(--white);
    font-weight: 600;
    font-size: 40px;
    line-height: 52px;
    letter-spacing: -0.2px;
  }
  .brand {
    position: absolute;
    left: 742px;
    top: 128px;
    display: flex;
    align-items: center;
    gap: 14px;
  }
  .brand__dot {
    width: 44px;
    height: 44px;
    border-radius: 50%;
    background: var(--blue-mid);
    flex: none;
  }
  .brand__name {
    color: var(--navy-text);
    font-weight: 600;
    font-size: 24px;
    line-height: 29px;
  }
  .headline-main {
    position: absolute;
    left: 24px;
    top: 252px;
    color: var(--red);
    font-weight: 800;
    font-size: 126px;
    line-height: 136px;
    letter-spacing: -2px;
  }
  .headline-sub {
    position: absolute;
    left: 28px;
    top: 392px;
    color: var(--navy-text);
    font-weight: 600;
    font-size: 43px;
    line-height: 54px;
    letter-spacing: -0.5px;
    white-space: nowrap;
  }
  .event-date {
    position: absolute;
    left: 28px;
    top: 648px;
    color: var(--white);
    font-weight: 600;
    font-size: 52px;
    line-height: 66px;
    white-space: nowrap;
  }
  .event-date__first { padding-left: 13px; }
  .event-venue {
    position: absolute;
    left: 28px;
    top: 808px;
    color: var(--navy-text);
    font-weight: 600;
    font-size: 39px;
    line-height: 50px;
  }
  .event-directions {
    position: absolute;
    left: 28px;
    top: 932px;
    color: var(--white);
    font-weight: 400;
    font-size: 21px;
    line-height: 29px;
  }
  .tagline {
    position: absolute;
    left: 38px;
    top: 1052px;
    color: var(--navy-text);
    font-weight: 700;
    font-style: italic;
    font-size: 34px;
    line-height: 46px;
  }
  .milestone {
    position: absolute;
    left: 28px;
    top: 1128px;
    color: var(--white);
    font-weight: 400;
    font-size: 21px;
    line-height: 30px;
  }
</style>
</head>
<body>
<main class="flyer">
  <svg class="flyer__shapes" viewBox="0 0 1017 1200" aria-hidden="true">
    <defs>
      <linearGradient id="header-band-fill" x1="0" y1="0" x2="1" y2="0">
        <stop offset="0" stop-color="#1a8bbb"/>
        <stop offset="1" stop-color="#0d4866"/>
      </linearGradient>
      <filter id="curve-shadow" x="-10%" y="-10%" width="130%" height="130%">
        <feGaussianBlur stdDeviation="8"/>
      </filter>
    </defs>
    <path d="M0,0 H1017 V98 C760,84 500,150 0,237 Z" fill="url(#header-band-fill)"/>
    <path d="M0,237 C500,150 760,84 1017,98 V108 C760,100 520,170 0,268 Z" fill="#ffffff"/>
    <path d="M0,495 C440,490 880,790 912,1200 L0,1200 Z" fill="#8a8a8a" opacity="0.45" filter="url(#curve-shadow)"/>
    <path d="M0,490 C440,486 872,790 902,1200 L0,1200 Z" fill="#ffffff"/>
    <path d="M0,500 C430,500 850,790 884,1200 L0,1200 Z" fill="var(--blue-deep)"/>
    <path d="M0,500 C380,500 750,760 770,1200 L0,1200 Z" fill="var(--blue-light)"/>
  </svg>

  <div class="molecule-art" role="img" aria-label="Faint molecular network illustration in soft lilac and pink"></div>

  <p class="headline-intro">CELEBRATE THE<br>INTERNATIONAL DAY<br>OF</p>

  <div class="brand">
    <span class="brand__dot"></span>
    <span class="brand__name">Halden<br>Lumaris Institute</span>
  </div>

  <h1 class="headline-main">AWESOMENESS</h1>

  <p class="headline-sub">BY CELEBRATING AWESOMENESS IN THE LABS<br>OF THE HALDEN LUMARIS INSTITUTE</p>

  <p class="event-date"><span class="event-date__first">MARCH 24TH, 2017</span><br>FROM 4-6PM</p>

  <p class="event-venue">Halvern Medical Education<br>Center Atrium</p>

  <p class="event-directions">(You can get to the Atrium from the Drentby<br>elevators by getting off on the 5th floor or from<br>the Crestmoor Pavilion elevators by getting off on the 5th floor).</p>

  <p class="tagline">We have a lot to celebrate!</p>

  <p class="milestone">Lumaris Institute just became and Institute in January 2017!</p>
</main>
</body>
</html>
```